Website Design AI Digital Marketing Tool for Small Businesses

We are a marketing saas that is selling an app that allows business owners to launch digital marketing campaigns in one click. Our value proposition is to help them grow their business in one click with pre-vetted marketers armed with AI.

We want a modern website design that looks like a professional tech startup / saas. Use the same content on brevora.io and make it look incredible. We want it to stand out and use big bold colors and text so that it's energetic and creative but still modern.

Pages are:
Home - brevora.io
Pricing - brevora.io/pricing
Features - https://brevora.io/features/
Marketing - https://brevora.io/marketing/

EXAMPLES
https://quandle.sitebuildr.io/
https://harbor-venture-sitebuildr-layout.sitebuildr.io/home-02

We really want a professional tech company feel. It needs to look like the best company with the best team in the world created it.

Target Market(s)

We are targeting small businesses to help them with their digital marketing

Industry/Entity Type

Tech

Coding

Coded - Design and coding required

Number of Pages Required

4 page

Font styles to use
Sans Serif
Other font styles liked:
• Work Sans

Colors
0094D4
00A9DD
6FCCEA
C7EBF8
E9F6FB

Requirements
Must have
• Modern, bright colors, same / similar content as existing site
Nice to have
• Big bold text and brand colors like plumtrex - but also techy and modern
Should not have
• nothing that doesnt fit the brand

```html
<!DOCTYPE html>
<html lang="en">
<head>
<meta charset="utf-8">
<title>Brevora — The App to Automate Your Business Growth</title>
<link rel="stylesheet" href="https://fonts.googleapis.com/css2?family=Montserrat:wght@400;500;600;700;800&display=swap">
<style>
:root{
  --ink:#000;
  --panel:#0c1a1e;
  --panel-2:#0f2226;
  --teal:#19d3e2;
  --teal-deep:#0a8c98;
  --teal-glow:rgba(10,160,170,.35);
  --text:#ffffff;
  --muted:#c8d4d6;
  --band-1:#0a1a5a;
  --band-2:#07245e;
  --paper:#ffffff;
}
*{box-sizing:border-box;margin:0;padding:0}
html,body{width:1200px;height:5064px;overflow:hidden;background:var(--paper)}
body{font-family:"Montserrat",sans-serif;color:var(--text);position:relative}
.page{position:absolute;left:43px;top:0;width:1112px;height:4770px;background:var(--ink);overflow:hidden}
.page > *{position:absolute}
.glow{border-radius:50%;filter:blur(60px);background:var(--teal-glow)}
.center{left:0;width:1112px;text-align:center}
.btn{display:flex;align-items:center;justify-content:center;border:2px solid var(--teal);border-radius:22px;color:var(--teal);font-size:13px;font-weight:600}
.btn.solid{background:var(--teal-deep);color:#e8fbfd;border-color:var(--teal)}
/* nav */
.logo{display:flex;align-items:center;gap:8px;font-size:36px;font-weight:500;color:var(--text)}
.logo .mark{width:34px;height:34px;border:3px solid var(--teal);border-radius:8px}
.nav a{position:absolute;top:40px;font-size:14px;font-weight:500;color:var(--text);text-decoration:none}
.nav a.active{color:var(--teal)}
/* hero */
.kicker{font-size:26px;font-weight:400}
.headline{font-size:62px;font-weight:800;color:var(--teal);letter-spacing:.5px}
.dash{left:331px;top:270px;width:448px;height:271px;border-radius:16px;border:6px solid #3a4246;background:linear-gradient(160deg,#1a2230,#0b1018 60%,#10141c)}
.lede{font-size:16px;line-height:22px;color:var(--muted)}
/* partners */
.partners{left:89px;top:803px;width:980px;height:43px;display:flex;align-items:center;justify-content:space-between}
.partners .label{border-left:3px solid var(--teal);padding-left:16px;font-size:12px;line-height:14px;font-weight:500}
.partners .label b{color:var(--teal);font-weight:600}
.partner{font-size:21px;font-weight:600;color:var(--text);display:flex;align-items:center;gap:6px}
.partner i{width:14px;height:14px;border-radius:50%;background:var(--teal);display:inline-block}
/* section headings */
.h2{font-size:36px;font-weight:700;line-height:48px}
.sub{font-size:18px;line-height:25px;color:var(--muted)}
/* steps */
.step{width:256px;height:269px;border:2px solid var(--teal);border-radius:8px;background:linear-gradient(180deg,#0a1416,#000);text-align:center;padding:30px 20px 0}
.step svg{width:46px;height:46px}
.step .num{font-size:15px;font-weight:700;margin-top:10px}
.step h3{font-size:16px;font-weight:700;margin:6px 0 8px}
.step p{font-size:14px;line-height:19px;color:var(--muted)}
/* best */
.best-title{font-size:46px;font-weight:800}
.best-title span{color:var(--teal)}
.art{left:98px;top:2203px;width:335px;height:394px;border-radius:30px;background:radial-gradient(circle at 50% 50%,#1f8fd0 0%,#0b3a66 40%,#000 75%)}
.benefit{left:521px;width:545px;height:151px;border-radius:8px;background:var(--panel);display:flex;align-items:center;padding:0 28px;gap:34px}
.benefit svg{flex:none;width:66px;height:66px}
.benefit h4{font-size:21px;font-weight:700;color:var(--teal);margin-bottom:8px}
.benefit p{font-size:16px;line-height:20px;color:var(--muted)}
/* video */
.video{left:89px;top:3006px;width:936px;height:289px;border-radius:8px;background:linear-gradient(90deg,#2a3a8a 0%,#4a5db0 45%,#b8bed6 100%);overflow:hidden}
.video .title{position:absolute;left:161px;top:44px;font-size:38px;line-height:47px;font-weight:500;color:#d7dcf2}
.video .caption{position:absolute;left:161px;top:252px;font-size:11px;line-height:17px;color:#b7c0ea}
.video .play{position:absolute;left:424px;top:111px;width:62px;height:62px;border-radius:50%;background:var(--teal);display:flex;align-items:center;justify-content:center}
/* stats */
.stats{left:89px;top:3379px;width:936px;height:178px;border-radius:8px;background:var(--panel);display:flex;justify-content:space-around;align-items:center;padding:0 60px}
.stat{text-align:center}
.stat b{display:block;font-size:52px;font-weight:800;color:var(--teal);line-height:60px}
.stat span{font-size:16px;font-weight:600;line-height:20px;display:block}
/* testimonials */
.quote{top:3773px;border-left:2px solid var(--teal);padding-left:20px}
.quote p{font-size:15px;line-height:21px;color:var(--muted)}
.who{display:flex;align-items:center;gap:12px;margin-top:22px;position:relative}
.avatar{width:56px;height:56px;border-radius:50%;background:linear-gradient(135deg,#8a8f95,#3b4046)}
.who b{font-size:17px;font-weight:700;display:block}
.who small{font-size:14px;line-height:22px;color:var(--muted)}
.qmark{position:absolute;font-size:120px;font-weight:800;color:var(--teal);line-height:1;top:-14px}
/* cta */
.cta{left:0;top:4180px;width:1112px;height:260px;background:linear-gradient(90deg,var(--band-1),var(--band-2) 50%,var(--band-1))}
.cta h2{font-size:34px;font-weight:700}
.cta h2 span{color:var(--teal)}
/* footer */
.footer-col{top:4512px;font-size:13px;line-height:28px}
.footer-col h5{font-size:13px;font-weight:700;color:var(--teal);line-height:16px;margin-bottom:10px}
.social{display:flex;gap:30px;left:150px;top:4608px}
.social i{width:24px;height:24px;border-radius:50%;background:var(--text);display:block}
.contact{left:895px;top:4506px;font-size:13px;line-height:16px}
.contact div{display:flex;gap:14px;margin-bottom:18px}
</style>
</head>
<body>
<main class="page">
  <div class="glow" style="left:-120px;top:120px;width:520px;height:520px"></div>
  <div class="glow" style="left:650px;top:1050px;width:380px;height:300px"></div>
  <div class="glow" style="left:-80px;top:2900px;width:1250px;height:520px;opacity:.7"></div>

  <!-- navigation -->
  <div class="logo" style="left:87px;top:24px"><span class="mark"></span>brevora</div>
  <nav class="nav" style="left:0;top:0;width:1112px;height:80px">
    <a class="active" style="left:387px">Home</a>
    <a style="left:513px">Pricing ⌄</a>
    <a style="left:660px">Features</a>
  </nav>
  <div class="btn" style="left:866px;top:30px;width:159px;height:41px">Get Started</div>

  <!-- hero -->
  <p class="kicker center" style="top:124px">The App to Automate Your</p>
  <h1 class="headline center" style="top:152px">Business Growth</h1>
  <div class="dash" role="img" aria-label="Analytics dashboard preview with line chart and marketing roadmap table">
    <svg width="436" height="259" viewBox="0 0 436 259">
      <rect x="0" y="0" width="86" height="259" fill="#0a0e15"/>
      <g fill="#5b6472"><rect x="18" y="30" width="44" height="4"/><rect x="18" y="48" width="38" height="4"/><rect x="18" y="66" width="40" height="4"/><rect x="18" y="84" width="36" height="4"/><rect x="18" y="102" width="42" height="4"/><rect x="18" y="120" width="38" height="4"/><rect x="18" y="138" width="46" height="4"/></g>
      <rect x="104" y="30" width="40" height="5" fill="#8a93a1"/>
      <polyline points="110,110 135,90 160,120 190,70 220,118 250,80 280,116 310,72 340,108 370,84 405,60" fill="none" stroke="#e6ecf5" stroke-width="2"/>
      <g fill="#fff"><circle cx="190" cy="70" r="3"/><circle cx="250" cy="80" r="3"/><circle cx="310" cy="72" r="3"/><circle cx="370" cy="84" r="3"/></g>
      <rect x="104" y="170" width="300" height="1" fill="#2c3440"/>
      <rect x="104" y="186" width="300" height="22" fill="#151b27"/>
      <rect x="104" y="216" width="300" height="22" fill="#10151f"/>
    </svg>
  </div>
  <p class="lede center" style="top:597px">The Only Marketing Platform for Small Businesses<br>that Handles Your Marketing in One Click.</p>
  <div class="btn solid" style="left:384px;top:683px;width:157px;height:41px">Get Started</div>
  <div class="btn" style="left:573px;top:683px;width:157px;height:41px">How It Works</div>

  <!-- partners -->
  <div class="partners">
    <div class="label">COMPANIES<br><b>WE WORK WITH:</b></div>
    <span class="partner">Nimbus Launch</span>
    <span class="partner">RankForge</span>
    <span class="partner"><i></i>Searchly Partner</span>
    <span class="partner">TradeLedger</span>
    <span class="partner">FunnelCore Academy</span>
  </div>

  <!-- steps -->
  <h2 class="h2 center" style="top:912px">Online Marketing<br>will never be the same</h2>
  <p class="sub center" style="top:1019px">Get a Fortune-500 Quality Web Presence<br>and a Personalized Action Plan</p>

  <article class="step" style="left:89px;top:1123px">
    <svg viewBox="0 0 46 46" fill="none" stroke="#19d3e2" stroke-width="3"><circle cx="23" cy="20" r="16"/><circle cx="23" cy="20" r="9"/><circle cx="23" cy="20" r="3"/><path d="M15 34l-3 10M31 34l3 10"/></svg>
    <div class="num">1.</div><h3>Set Your Goals</h3>
    <p>The easiest intake form that you've ever seen. Set your goals and click submit for a custom proposal.</p>
  </article>
  <article class="step" style="left:427px;top:1123px">
    <svg viewBox="0 0 46 46" fill="none" stroke="#19d3e2" stroke-width="3"><rect x="4" y="6" width="38" height="34" rx="3"/><path d="M4 14h38M14 14v26M20 22h16v12H20z"/></svg>
    <div class="num">2.</div><h3>Get Detailed Action Plan</h3>
    <p>Get Your Granular Action Plan / Proposal That Fits Your Parameters to Take You to the Next Level.</p>
  </article>
  <article class="step" style="left:769px;top:1123px">
    <svg viewBox="0 0 46 46" fill="none" stroke="#19d3e2" stroke-width="3"><circle cx="25" cy="26" r="15"/><path d="M25 26l6-6M21 6h8M4 20h8M2 27h8M5 34h8"/></svg>
    <div class="num">3.</div><h3>Instant Marketing</h3>
    <p>Instantly Get Matched With One of the Top Marketing Pros in Your Industry to Help You Execute Your Campaign.</p>
  </article>
  <article class="step" style="left:91px;top:1456px">
    <svg viewBox="0 0 46 46" fill="none" stroke="#19d3e2" stroke-width="3"><rect x="4" y="4" width="38" height="30" rx="2" stroke-dasharray="4 3"/><path d="M10 24l7-8 6 6 6-10 7 12M16 42h14"/></svg>
    <div class="num">4.</div><h3>AI+ Web Creation</h3>
    <p>AI Generated Marketing Campaigns &amp; Website Draft Will Be Generated to Use As a Starting Point.</p>
  </article>
  <article class="step" style="left:427px;top:1456px">
    <svg viewBox="0 0 46 46" fill="none" stroke="#19d3e2" stroke-width="3"><path d="M6 6h18l16 16-18 18L6 24z"/><circle cx="15" cy="15" r="3"/></svg>
    <div class="num">5.</div><h3>Flexible Pricing</h3>
    <p>No long term commitments or contracts. Subscribe month to month or only pay for what you need.</p>
  </article>
  <article class="step" style="left:769px;top:1456px">
    <svg viewBox="0 0 46 46" fill="none" stroke="#19d3e2" stroke-width="3"><path d="M23 3c8 8 9 20 4 30h-8C14 23 15 11 23 3z"/><circle cx="23" cy="17" r="3"/><path d="M19 33l-6 6M27 33l6 6M23 36v8"/></svg>
    <div class="num">6.</div><h3>Launch Campaign</h3>
    <p>Launch your marketing / business growth campaign and stay in contact to get outstanding results.</p>
  </article>

  <div class="btn" style="left:478px;top:1784px;width:158px;height:41px">View Pricing</div>
  <div class="btn" style="left:478px;top:1859px;width:158px;height:41px">What's Included</div>

  <!-- simply the best -->
  <h2 class="best-title" style="left:130px;top:1984px">Simply <span>the Best</span></h2>
  <p class="sub" style="left:130px;top:2055px;width:880px;color:#fff">The All in One Platform to Generate Personalized Suggestions and Hire Your Dream Team to Launch Winning Campaigns.</p>
  <div class="art" role="img" aria-label="Isometric illustration of glowing app screens and analytics panels"></div>

  <div class="benefit" style="top:2160px">
    <svg viewBox="0 0 66 66" fill="none" stroke="#19d3e2" stroke-width="4"><circle cx="33" cy="33" r="29"/><path d="M20 34l9 9 18-19"/></svg>
    <div><h4>No More Broken Promises</h4><p>We guarantee quality marketing professionals that deliver on time and communicate constantly.</p></div>
  </div>
  <div class="benefit" style="top:2341px">
    <svg viewBox="0 0 66 66" fill="none" stroke="#19d3e2" stroke-width="4"><circle cx="33" cy="33" r="29"/><path d="M20 34l9 9 18-19"/></svg>
    <div><h4>Start at Nearly Any Budget</h4><p>Simple, dynamic pricing within the budget you select. Only pay for what you use.</p></div>
  </div>
  <div class="benefit" style="top:2522px">
    <svg viewBox="0 0 66 66" fill="none" stroke="#19d3e2" stroke-width="4"><circle cx="33" cy="33" r="29"/><path d="M20 34l9 9 18-19"/></svg>
    <div><h4>Transparency &amp; Control</h4><p>View campaign progress and update preferences at any time through our convenient application.</p></div>
  </div>

  <!-- video -->
  <h2 class="h2 center" style="top:2753px;line-height:41px">Watch Brevora AI Build<br>an SEO Optimized<br>Website in Minutes.</h2>
  <p class="sub center" style="top:2898px;color:#fff">Receive an Professional Designed Website Same Day*</p>
  <div class="video" role="img" aria-label="Video preview: laptop on a desk with a finance platform headline">
    <div class="title">Empowering Small<br>Businesses With<br>Enterprise Finance<br>Solutions</div>
    <div class="caption">We're Revolutionizing Finance: Machine Learning for Precision<br>Accounting &amp; Projections</div>
    <div class="play"><svg width="22" height="24" viewBox="0 0 22 24"><path d="M3 2l17 10L3 22z" fill="#fff"/></svg></div>
  </div>

  <!-- stats -->
  <div class="stats">
    <div class="stat"><b>4k+</b><span>WEBSITES<br>BUILT</span></div>
    <div class="stat"><b>2k</b><span>CONSULTING<br>HRS</span></div>
    <div class="stat"><b>&lt;1 Hr</b><span>AVG RESPONSE<br>TIME</span></div>
    <div class="stat"><b>99%</b><span>SATISFACTION<br>RATE</span></div>
  </div>

  <!-- testimonials -->
  <h2 class="h2 center" style="top:3625px">What People Are Saying</h2>
  <p class="sub center" style="top:3692px;color:#fff">Just a Few Out of Thousands of Happy Customers.</p>

  <figure class="quote" style="left:89px;width:324px">
    <p>Brevora did an excellent job recreating our website and is doing an excellent job servicing our account as well. I would highly recommend Brevora for any business.</p>
    <div class="who"><span class="avatar"></span><div><b>Marcus T</b><small>Owner</small></div><span class="qmark" style="left:180px">“</span></div>
  </figure>
  <figure class="quote" style="left:419px;width:325px">
    <p>Brevora's team has been incredible to work with. The best part is that they have delivered customers to our door. The results of our initial campaign with them have surpassed all of our expectations and we hope to continue this partnership for a long time to come!</p>
    <div class="who"><span class="avatar"></span><div><b>Owen R.</b><small>Gold &amp; Coin<br>Dealer</small></div><span class="qmark" style="left:180px">“</span></div>
  </figure>
  <figure class="quote" style="left:754px;width:325px">
    <p>The migration was just as smooth as the whole experience has been working with them. I am looking forward to continuing our partnership! They'll be right there with me when I begin redesign of my website. Highly recommend Brevora for your website needs!!</p>
    <div class="who"><span class="avatar"></span><div><b>Nadia P.</b><small>Business<br>Consultant</small></div><span class="qmark" style="left:180px">“</span></div>
  </figure>

  <!-- call to action -->
  <section class="cta" role="img" aria-label="Blue band with circuit line decoration">
    <h2 class="center" style="position:absolute;top:52px">Let’s Make Something Great <span>Together</span></h2>
    <p class="sub center" style="position:absolute;top:110px;color:#fff">Just a Few Out of Thousands of Happy Customers.</p>
    <div class="btn solid" style="position:absolute;left:478px;top:159px;width:197px;height:40px">Join The Revolution</div>
  </section>

  <!-- footer -->
  <div class="logo" style="left:91px;top:4516px;font-size:46px"><span class="mark" style="width:44px;height:44px"></span>brevora</div>
  <div class="social"><i aria-label="Social link"></i><i aria-label="Social link"></i><i aria-label="Social link"></i></div>
  <div class="footer-col" style="left:386px"><h5>Quick<br>Links</h5>Marketing<br>Web Creation<br>Automation</div>
  <div class="footer-col" style="left:525px"><h5>Account<br>Management</h5>Login<br>Account<br>Support</div>
  <div class="footer-col" style="left:671px"><h5>Important<br>Links</h5>Privacy Policy<br>Terms &amp; Conditions</div>
  <div class="contact">
    <div><svg width="18" height="22" viewBox="0 0 18 22" fill="none" stroke="#19d3e2" stroke-width="2"><path d="M9 21s7-7 7-12A7 7 0 0 0 2 9c0 5 7 12 7 12z"/><circle cx="9" cy="9" r="2.5"/></svg><span>418 Linden Ave<br>#305 Riverton, GA<br>30421</span></div>
    <div><svg width="18" height="18" viewBox="0 0 18 18" fill="none" stroke="#19d3e2" stroke-width="2"><circle cx="9" cy="9" r="3"/><path d="M12 9v1.5a2.5 2.5 0 0 0 5 0V9a8 8 0 1 0-3 6.2"/></svg><span>hello@brevora.io</span></div>
  </div>
  <p class="center" style="top:4676px;font-size:12px">© Copyright 2024 Brevora AI INC</p>
</main>
</body>
</html>
```